Loan broker seeks referral card design for real estate financing

We need a design for a referral card for people who recommend us for real estate financing. If the deal goes through, each referrer will receive €750.

Text similar to: Recommend me! For every successful real estate financing referral, you will receive €750. (Other suggestions are also welcome)

The size should be no larger than A5 format, or possibly even oblong.
The design should convey security and competence and include themes such as independent advice.

The design should also include the company logo and a photo of me. Naturally, the design should also include a link to my website: www.die-brennholt.at, along with my phone number and email address: office@die-brennholt.at

```html
<!DOCTYPE html>
<html lang="de">
<head>
<meta charset="utf-8">
<title>Tippgeberbonus Karte – BH Vermögensberatung</title>
<link rel="stylesheet" href="https://fonts.googleapis.com/css2?family=Cinzel:wght@500;600&family=Montserrat:wght@400;500;700&display=swap">
<style>
  :root {
    --blue: #2c5bab;
    --blue-deep: #1f3f7e;
    --gold-dark: #c49a4e;
    --gold-mid: #e3c27a;
    --gold-light: #f6e2a8;
    --white: #ffffff;
    --navy-suit: #2a2a3a;
    --page: #efeae0;
  }
  * { margin: 0; padding: 0; box-sizing: border-box; }
  html, body { width: 1200px; height: 715px; overflow: hidden; background: var(--page); }
  .card {
    position: absolute; left: 10px; top: 20px;
    width: 1180px; height: 674px;
    background: var(--white); overflow: hidden;
    font-family: "Montserrat", Arial, sans-serif; color: var(--white);
  }
  .card__field { position: absolute; left: 0; top: 0; width: 1180px; height: 574px; background: var(--blue); }
  .abs { position: absolute; white-space: nowrap; line-height: 1; }

  .brand__ring { left: 43px; top: 42px; width: 140px; height: 140px; border: 6px solid var(--white); border-radius: 50%; }
  .brand__divider { left: 197px; top: 43px; width: 4px; height: 139px; background: var(--white); }
  .brand__name { left: 211px; top: 86px; font-size: 27px; font-weight: 700; letter-spacing: -0.2px; }
  .brand__tagline { left: 209px; top: 118px; font-size: 19px; font-weight: 700; }

  .headline { left: 44px; top: 221px; font-family: "Cinzel", Georgia, serif; font-weight: 600; font-size: 39px; letter-spacing: 0.5px;
    background: linear-gradient(90deg, var(--gold-mid), var(--gold-light) 45%, var(--gold-mid) 80%, var(--gold-dark));
    -webkit-background-clip: text; background-clip: text; color: transparent; }
  .offer { left: 43px; top: 267px; font-size: 25.5px; letter-spacing: 0.3px; }
  .offer__amount { left: 43px; top: 299px; font-size: 25.5px; font-weight: 700; }

  .bonus-band { left: 0; top: 339px; width: 720px; height: 39px; background: var(--white); }
  .bonus-band__text { left: 43px; top: 350px; font-family: "Cinzel", Georgia, serif; font-weight: 500; font-size: 24.5px; color: var(--blue); letter-spacing: 0.2px; }

  .benefits { left: 43px; top: 402px; list-style: none; }
  .benefits li { display: flex; align-items: center; height: 32.5px; font-size: 25.5px; letter-spacing: 0.3px; }
  .benefits svg { width: 24px; height: 20px; margin-right: 12px; }
  .benefits strong { font-weight: 700; }

  .portrait { left: 792px; top: 39px; width: 388px; height: 535px;
    background: radial-gradient(ellipse 38% 30% at 58% 35%, #e0a88f 0%, #c98d76 60%, transparent 62%),
                linear-gradient(180deg, transparent 55%, var(--navy-suit) 56%);
    clip-path: polygon(0 100%, 20% 70%, 27% 12%, 45% 0, 70% 2%, 82% 25%, 83% 62%, 100% 70%, 100% 100%); }

  .badge { left: 691px; top: 270px; width: 152px; height: 152px; border-radius: 50%;
    background: radial-gradient(circle at 45% 35%, var(--gold-light), var(--gold-mid) 60%, var(--gold-dark));
    color: var(--blue); text-align: center; }
  .badge__amount { position: absolute; left: 0; right: 0; top: 30px; font-size: 42px; font-weight: 700; letter-spacing: -1px; }
  .badge__label { position: absolute; left: 0; right: 0; top: 77px; font-size: 19.5px; font-weight: 500; line-height: 1.3; }

  .contact-bar { left: 0; top: 519px; width: 1088px; height: 98px;
    background: linear-gradient(90deg, var(--gold-dark), var(--gold-light) 30%, var(--gold-mid) 55%, var(--gold-light) 75%, var(--gold-mid));
    clip-path: polygon(0 0, 100% 0, 90.3% 100%, 0 100%); }
  .contact { top: 551px; display: flex; align-items: center; font-size: 25.5px; font-weight: 500; color: var(--blue); }
  .contact__icon { width: 30px; height: 30px; margin-right: 6px; }
  .contact--web { left: 42px; }
  .contact--phone { left: 370px; }
  .contact--mail { left: 657px; }
</style>
</head>
<body>
<div class="card">
  <div class="card__field"></div>

  <div class="abs brand__ring"></div>
  <div class="abs brand__divider"></div>
  <div class="abs brand__name">BH Vermögensberatung GmbH</div>
  <div class="abs brand__tagline">Finanzieren, Versichern, Vorsorgen</div>

  <div class="abs headline">EMPFEHLEN SIE MICH WEITER!</div>
  <div class="abs offer">Für jede erfolgreiche Immobilienfinanzierung</div>
  <div class="abs offer__amount">erhalten Sie €750</div>

  <div class="abs bonus-band"></div>
  <div class="abs bonus-band__text">SICHERN SIE IHREN TIPPGEBERBONUS!</div>

  <ul class="abs benefits">
    <li><svg viewBox="0 0 24 20"><path d="M2 10l7 7L22 3" fill="none" stroke="#e3c27a" stroke-width="4"/></svg><span><strong>Unabhängige</strong> und kompetente Beratung</span></li>
    <li><svg viewBox="0 0 24 20"><path d="M2 10l7 7L22 3" fill="none" stroke="#e3c27a" stroke-width="4"/></svg><span><strong>Beste Konditionen</strong> dank großer Marktübersicht</span></li>
    <li><svg viewBox="0 0 24 20"><path d="M2 10l7 7L22 3" fill="none" stroke="#e3c27a" stroke-width="4"/></svg><span><strong>Persönliche</strong> Unterstützung bei der Finanzierung</span></li>
  </ul>

  <div class="abs portrait" role="img" aria-label="Porträtfoto des Beraters im dunklen Sakko und weißem Hemd"></div>

  <div class="abs badge">
    <div class="badge__amount">€750</div>
    <div class="badge__label">TIPPGEBER<br>BONUS!</div>
  </div>

  <div class="abs contact-bar"></div>
  <div class="abs contact contact--web">
    <svg class="contact__icon" viewBox="0 0 30 30"><circle cx="15" cy="15" r="15" fill="#2c5bab"/><g fill="none" stroke="#e3c27a" stroke-width="1.6"><circle cx="15" cy="15" r="9"/><ellipse cx="15" cy="15" rx="4" ry="9"/><path d="M6 15h18M8 10h14M8 20h14"/></g></svg>
    <span>www.die-brennholt.at</span>
  </div>
  <div class="abs contact contact--phone">
    <svg class="contact__icon" viewBox="0 0 30 30"><circle cx="15" cy="15" r="15" fill="#2c5bab"/><path d="M10 7l3 4-2 2c1 2 3 4 5 5l2-2 4 3-2 3c-6 0-13-7-13-13z" fill="#f6e2a8"/></svg>
    <span>+43 676 123 4567</span>
  </div>
  <div class="abs contact contact--mail">
    <svg class="contact__icon" viewBox="0 0 30 30"><circle cx="15" cy="15" r="15" fill="#2c5bab"/><rect x="8" y="10" width="14" height="10" rx="1.5" fill="none" stroke="#f6e2a8" stroke-width="1.8"/><path d="M8.5 11l6.5 5 6.5-5" fill="none" stroke="#f6e2a8" stroke-width="1.8"/></svg>
    <span>office@die-brennholt.at</span>
  </div>
</div>
</body>
</html>
```